Kestrel Works Business Cards

This job is for the design of a business card.
I would like to review the design in 2x colour tones to choose from black and white inverted.
EG:
Black with white logo and white with black logo on BACK
White with black text on front and black with white text options
PRINTING DIMENSIONS: 4.5 x 8.5cm
Complete design will need to be provided in ready to print format with bleed lines
Target Market(s)
The audience of my business are people in the trade industry.
It will be also used for general networking with trades people and possible future clients.
I want to be represented as a professional, dynamic, creative and personable operator.
The card should reflect style, taste, experience, professionalism.
Industry/Entity Type
Business
Requirements
Must have
- BACK CONTENT:
- Logo in white and black background and vice versa with WHITE card and black logo review samples.
- FRONT CARD CONTENT:
- Name: Morgan Telvane
- Director
- Phone: 0438 216 947
- Email: morgan@kestrelworks.com.au
- Web: kestrelworks.com.au
- LICENCE #: KT-R 72158
Nice to have
- Possibly a textured background design on rear as a pose to a solid black
- Possibly adding a blue or orange discreet colour tone (possibly for email, phone abbreviated letter or symbols).

```html
<!DOCTYPE html>
<html lang="en">
<head>
<meta charset="utf-8">
<title>Kestrel Works Business Cards</title>
<link rel="stylesheet" href="https://fonts.googleapis.com/css2?family=Questrial&display=swap">
<style>
  :root {
    --page: #ffffff;
    --ink: #231f20;
    --paper: #ffffff;
    --reverse: #ffffff;
    --accent: #f7941d;
    --shadow: #2b2b2b;
  }
  * { margin: 0; padding: 0; box-sizing: border-box; }
  html, body { width: 960px; height: 1200px; overflow: hidden; background: var(--page); }
  body { position: relative; font-family: "Questrial", "Helvetica Neue", Arial, sans-serif; }

  .card {
    position: absolute;
    left: 119px;
    width: 736px;
    overflow: hidden;
    box-shadow: 6px 6px 2px var(--shadow);
  }
  .card--back { top: 138px; height: 404px; background: var(--ink); }
  .card--front { top: 620px; height: 402px; background: var(--paper); }

  .wordmark {
    position: absolute;
    text-align: center;
    color: var(--reverse);
    white-space: nowrap;
  }
  .wordmark__name { display: block; letter-spacing: 0.02em; line-height: 1; }
  .wordmark__tagline { display: block; letter-spacing: 0.42em; }

  .card--back .wordmark { left: 0; right: 0; top: 166px; }
  .card--back .wordmark__name { font-size: 50px; }
  .card--back .wordmark__tagline { font-size: 9px; margin-top: 6px; }

  .logo-band {
    position: absolute;
    left: 0;
    top: 139px;
    width: 331px;
    height: 104px;
    background: var(--ink);
    border-bottom: 7px solid var(--accent);
  }
  .logo-band .wordmark { left: 0; right: 0; top: 34px; }
  .logo-band .wordmark__name { font-size: 26px; }
  .logo-band .wordmark__tagline { font-size: 5px; margin-top: 4px; letter-spacing: 0.4em; }

  .holder {
    position: absolute;
    left: 455px;
    top: 62px;
    color: var(--ink);
    white-space: nowrap;
  }
  .holder__name { display: block; font-size: 22px; line-height: 26px; }
  .holder__role { display: block; font-size: 13px; line-height: 18px; letter-spacing: 0.2em; text-transform: uppercase; }

  .contact {
    position: absolute;
    left: 455px;
    top: 122px;
    list-style: none;
    font-size: 18px;
    color: var(--ink);
    white-space: nowrap;
  }
  .contact li { height: 39px; line-height: 28px; }
  .contact__link { color: var(--accent); }
</style>
</head>
<body>
  <section class="card card--back" aria-label="Card back">
    <div class="wordmark">
      <span class="wordmark__name">KESTREL WORKS</span>
      <span class="wordmark__tagline">CONSTRUCTION GROUP</span>
    </div>
  </section>

  <section class="card card--front" aria-label="Card front">
    <div class="logo-band">
      <div class="wordmark">
        <span class="wordmark__name">KESTREL WORKS</span>
        <span class="wordmark__tagline">CONSTRUCTION GROUP</span>
      </div>
    </div>
    <div class="holder">
      <span class="holder__name">Morgan Telvane</span>
      <span class="holder__role">Director</span>
    </div>
    <ul class="contact">
      <li>0438216947</li>
      <li class="contact__link">morgan@kestrelworks.com.au</li>
      <li class="contact__link">www.kestrelworks.com.au</li>
      <li>Licence : KT-R 72158</li>
    </ul>
  </section>
</body>
</html>
```